Business Cards

I'd like help creating business cards with the full logo "Veltrona Capital Partners" on the back of the card (navy background with white writing), and abbreviated logo "VCP" on the front. Would like to list name, title, phone number, email, and website listed on front of card. Would like to keep very simple. Front font Arial or similar.

```html
<!DOCTYPE html>
<html lang="en">
<head>
<meta charset="utf-8">
<title>Veltrona Capital Partners – Business Cards</title>
<link href="https://fonts.googleapis.com/css2?family=Work+Sans:wght@500;600;700&display=swap" rel="stylesheet">
<style>
  :root {
    --navy: #1f3567;
    --paper: #efefef;
    --white: #f4f4f4;
    --backdrop: #d9d9d9;
  }
  * { margin: 0; padding: 0; box-sizing: border-box; }
  html, body {
    width: 1200px; height: 934px; overflow: hidden;
    background: var(--backdrop);
    font-family: "Work Sans", Arial, sans-serif;
  }
  .card {
    position: absolute;
    width: 557px; height: 318px;
    border-radius: 14px;
    overflow: hidden;
  }
  /* Front */
  .card-front { left: 142px; top: 80px; background: var(--paper); }
  .name-band {
    position: absolute; left: 0; top: 57px;
    width: 247px; height: 82px;
    background: var(--navy);
    clip-path: polygon(0 0, 195px 0, 247px 100%, 0 100%);
  }
  .person-name {
    position: absolute; left: 21px; top: 76px;
    font-size: 26px; font-weight: 600; color: var(--white);
    letter-spacing: -0.2px; line-height: 1;
  }
  .person-title {
    position: absolute; left: 21px; top: 104px;
    font-size: 12.5px; font-weight: 500; color: var(--white);
    letter-spacing: -0.2px; line-height: 1;
  }
  .short-name {
    position: absolute; left: 380px; top: 58px;
    width: 155px; height: 79px;
    display: flex; align-items: center; justify-content: center;
    font-size: 56px; font-weight: 700; color: var(--navy);
    line-height: 1;
  }
  .contact-list { position: absolute; left: 20px; top: 205px; list-style: none; }
  .contact-item {
    display: flex; align-items: center; height: 33px;
    font-size: 15px; font-weight: 600; color: var(--navy);
  }
  .contact-icon { width: 26px; height: 26px; margin-right: 6px; flex: none; }
  .bottom-band {
    position: absolute; left: 0; bottom: 0;
    width: 100%; height: 15px; background: var(--navy);
  }
  /* Back */
  .card-back {
    left: 520px; top: 493px; background: var(--navy);
    display: flex; flex-direction: column; align-items: center; justify-content: center;
    color: var(--white); font-weight: 600;
  }
  .company-name {
    font-size: 50px; letter-spacing: 2px; line-height: 1;
  }
  .company-sub {
    margin-top: 22px;
    font-size: 21px; letter-spacing: 12.5px; line-height: 1;
    margin-right: -12.5px;
  }
</style>
</head>
<body>
  <section class="card card-front" aria-label="Business card front">
    <div class="name-band"></div>
    <p class="person-name">Owen Hartley</p>
    <p class="person-title">Co-Founder &amp; Managing Partner</p>
    <p class="short-name">VCP</p>

    <ul class="contact-list">
      <li class="contact-item">
        <svg class="contact-icon" viewBox="0 0 26 26" fill="none" stroke="#1f3567" stroke-width="1.5" stroke-linejoin="round">
          <path d="M5 3l4 0 2 5-3 2c1.5 3 4 5.5 7 7l2-3 5 2v4c0 1-1 2-2 2C11 22 4 15 3 5c0-1 1-2 2-2z"/>
        </svg>
        <span>555-204-7183</span>
      </li>
      <li class="contact-item">
        <svg class="contact-icon" viewBox="0 0 26 26" fill="none" stroke="#1f3567" stroke-width="1.5" stroke-linejoin="round">
          <rect x="4" y="11" width="18" height="12"/>
          <path d="M4 11l9 7 9-7M4 23l7-6M22 23l-7-6"/>
          <rect x="8" y="3" width="10" height="11"/>
          <circle cx="13" cy="8" r="2"/>
        </svg>
        <span>owen@veltronacp.com</span>
      </li>
      <li class="contact-item">
        <svg class="contact-icon" viewBox="0 0 26 26" fill="none" stroke="#1f3567" stroke-width="1.5">
          <circle cx="13" cy="13" r="11"/>
          <ellipse cx="13" cy="13" rx="5" ry="11"/>
          <path d="M2 13h22M4 7h18M4 19h18M13 2v22"/>
        </svg>
        <span>www.veltronacp.com</span>
      </li>
    </ul>
    <div class="bottom-band"></div>
  </section>

  <section class="card card-back" aria-label="Business card back">
    <p class="company-name">VELTRONA</p>
    <p class="company-sub">CAPITAL PARTNERS</p>
  </section>
</body>
</html>
```